Etikett für ein Erfrischungsgetränk
Zielgruppe
Veltrano ist ein Startup Unternehmen, welches in naher Zukunft ein
Hibiskus-Erfrischungsgetränk auf den Markt bringen möchte.
Die Zielgruppe ist jedermann. Ob jung oder alt.
Aufgabenstellung
Das Etikett einer 0,33 l Longneckflasche soll:
Erfrischend, Modern aber auch Zeitlos, Einzigartig, dezent wirken.
Das Logo soll hervorstehen und der Hintergrund dezent sein.
Vorderetikett: 76 mm breit, 86 mm hoch
Rücketikett: 55 mm breit, 75 mm hoch
Die Getränkfarbe ist rötlich.

```html
<!DOCTYPE html>
<html lang="de">
<head>
<meta charset="utf-8">
<title>Veltrano – Vorderetikett</title>
<link rel="stylesheet" href="https://fonts.googleapis.com/css2?family=Arimo:wght@400;700&display=swap">
<style>
  :root {
    --paper: #ffffff;
    --sky: #3fc3ea;
    --aqua: #48c6c9;
    --leaf: #6cbd5a;
    --lime: #c5d64a;
    --sun: #e9e14e;
    --magenta: #e5087e;
    --berry: #a3197f;
    --petal: #ee5b7c;
    --petal-deep: #d62a4d;
    --ink-light: #ffffff;
  }
  html, body {
    margin: 0;
    padding: 0;
    width: 1061px;
    height: 1200px;
    overflow: hidden;
    background: var(--paper);
  }
  .label {
    position: relative;
    width: 1061px;
    height: 1200px;
  }
  .label-art {
    position: absolute;
    inset: 0;
    display: block;
  }
  .brand-name {
    position: absolute;
    left: 0;
    right: 0;
    top: 360px;
    margin: 0;
    text-align: center;
    font-family: "Arimo", Arial, sans-serif;
    font-weight: 700;
    font-size: 190px;
    line-height: 1;
    color: var(--berry);
  }
  .product-claim {
    position: absolute;
    left: 0;
    right: 0;
    top: 722px;
    margin: 0;
    text-align: center;
    font-family: "Arimo", Arial, sans-serif;
    font-weight: 400;
    color: var(--ink-light);
  }
  .product-claim .claim-main {
    display: block;
    font-size: 46px;
    line-height: 1.2;
    margin-left: -20px;
  }
  .product-claim .claim-sub {
    display: block;
    font-size: 33px;
    line-height: 1.3;
    margin-top: 8px;
    margin-left: 40px;
    word-spacing: 6px;
  }
</style>
</head>
<body>
  <main class="label">
    <svg class="label-art" width="1061" height="1200" viewBox="0 0 1061 1200" aria-hidden="false">
      <defs>
        <linearGradient id="backdrop-wash" x1="0" y1="0" x2="0.35" y2="1">
          <stop offset="0" stop-color="var(--sky)"/>
          <stop offset="0.3" stop-color="var(--aqua)"/>
          <stop offset="0.55" stop-color="var(--leaf)"/>
          <stop offset="0.8" stop-color="var(--lime)"/>
          <stop offset="1" stop-color="var(--sun)"/>
        </linearGradient>
        <radialGradient id="flower-tone" cx="0.5" cy="0.5" r="0.5">
          <stop offset="0" stop-color="var(--petal-deep)"/>
          <stop offset="1" stop-color="var(--petal)"/>
        </radialGradient>
      </defs>

      <path class="label-shape"
            d="M8 155 H230 C300 40 420 4 530 4 C640 4 760 40 830 155 H1053
               Q1057 155 1057 162 V1190 Q1057 1196 1050 1196 H10
               Q4 1196 4 1190 V162 Q4 155 8 155 Z"
            fill="url(#backdrop-wash)"
            role="img" aria-label="Dezenter Aquarellhintergrund mit hellen Schwüngen in Türkis, Grün und Gelb"/>

      <ellipse class="hibiscus-flower" cx="440" cy="190" rx="140" ry="150"
               fill="url(#flower-tone)"
               role="img" aria-label="Rosa Hibiskusblüte"/>

      <path class="color-splash"
            d="M215 700 C260 680 330 695 380 690 C430 680 470 700 520 690
               C580 680 640 700 700 690 C760 700 800 730 790 780
               C800 830 770 860 730 850 C700 890 640 880 600 870
               C560 900 500 890 460 870 C420 895 360 890 330 860
               C280 880 230 860 225 815 C195 790 200 740 215 700 Z"
            fill="var(--magenta)"
            role="img" aria-label="Magentafarbener Farbspritzer als Hintergrund für den Produkthinweis"/>
    </svg>

    <h1 class="brand-name">Veltrano</h1>

    <p class="product-claim">
      <span class="claim-main">Erfrischungsgetränk</span>
      <span class="claim-sub">aus aufgebrühtem Hibiskustee</span>
    </p>
  </main>
</body>
</html>
```